Brightwell Giving Inc

We need a full re-design of our non-profit organization website (www.brightwellgiving.org). Ideally, we are looking to make it more attractive, user-friendly, and interactive with our business model.

Please make sure to user colors that ago with our logo.

We need a homepage done and we also need a content page done where we will use for the other pages to fill with content.

Target Market(s)

Clothes/textiles donations.

Industry/Entity Type

Charity

Number of Pages Required

2 page

Colors

Designer to choose colors to be used in the design.

Requirements
Must have
• It must match the styling of our logo and same colors as current website. (www.brightwellgiving.org)
Nice to have
• Sleek homepage that is easy to understand and get our main points across.

```html
<!DOCTYPE html>
<html lang="en">
<head>
<meta charset="utf-8">
<title>Brightwell Giving – Home</title>
<link rel="stylesheet" href="https://fonts.googleapis.com/css2?family=Playfair+Display:wght@400;700&family=Open+Sans:wght@400;600;700&display=swap">
<style>
:root{
  --green-dark:#3b6e1d;
  --green:#4f8f2a;
  --green-mid:#6cb24a;
  --green-light:#94d17f;
  --green-pale:#dcf1d2;
  --yellow:#ffd200;
  --red:#e01b1b;
  --ink:#2b2b2b;
  --grey-bg:#efefef;
  --white:#ffffff;
}
*{box-sizing:border-box;margin:0;padding:0}
html,body{width:1200px;height:3704px;overflow:hidden}
body{font-family:"Open Sans",Arial,sans-serif;color:var(--ink);background:var(--white);position:relative}
.serif{font-family:"Playfair Display",Georgia,serif}
section,header,nav,footer{position:absolute;left:0;width:1200px}
.btn-more{display:inline-block;background:var(--green-dark);color:var(--white);font-size:12px;font-weight:700;padding:7px 14px;border-radius:3px;letter-spacing:.3px;white-space:nowrap}
.logo-mark{display:inline-block;background:var(--yellow);border:3px solid var(--green)}

/* header */
.site-header{top:0;height:94px}
.brand{position:absolute;left:172px;top:24px;display:flex;align-items:center;gap:10px}
.brand .logo-mark{width:44px;height:44px}
.brand-name{font-family:"Playfair Display",Georgia,serif;font-weight:700;font-size:22px;color:var(--green-dark);line-height:1}
.brand-tag{font-size:11px;color:var(--ink);margin-top:4px}
.contact-phones{position:absolute;left:548px;top:26px;display:flex;gap:22px;align-items:center}
.phone-icon{width:34px;height:34px}
.phone-block{font-size:13px;line-height:1.25}
.phone-block b{display:block;font-size:15px}
.donate-now{position:absolute;left:891px;top:28px;background:var(--red);color:var(--white);font-weight:700;font-size:15px;padding:9px 20px;border-radius:18px}

/* nav */
.main-nav{top:94px;height:42px;background:var(--yellow)}
.main-nav ul{list-style:none;display:flex;position:absolute;left:170px;top:7px}
.main-nav li{font-size:13px;font-weight:600;padding:6px 15px;color:var(--ink)}
.main-nav li.active{background:var(--green-dark);color:var(--white)}

/* hero */
.hero{top:136px;height:501px;
  background:
    linear-gradient(90deg,rgba(20,30,15,.45) 0%,rgba(20,30,15,.15) 40%,rgba(0,0,0,0) 60%),
    radial-gradient(ellipse 120px 200px at 630px 250px,#4a2f22 0%,rgba(74,47,34,0) 100%),
    radial-gradient(ellipse 230px 210px at 600px 420px,#4f5a2c 0%,#5d6a36 40%,rgba(93,106,54,0) 100%),
    radial-gradient(ellipse 200px 140px at 880px 430px,#2fa3b3 0%,rgba(47,163,179,0) 100%),
    radial-gradient(ellipse 180px 150px at 1040px 420px,#e86f3a 0%,#d9482c 40%,rgba(217,72,44,0) 100%),
    radial-gradient(ellipse 140px 260px at 80px 320px,#3c5d9c 0%,#6f86b9 40%,rgba(111,134,185,0) 100%),
    radial-gradient(ellipse 110px 170px at 300px 230px,#caa081 0%,rgba(202,160,129,0) 100%),
    radial-gradient(ellipse 120px 180px at 830px 240px,#d9d6cf 0%,rgba(217,214,207,0) 100%),
    linear-gradient(180deg,#b9bdb0 0%,#cfcfc3 45%,#a7a58f 100%)}
.hero-title{position:absolute;left:172px;top:180px;color:var(--white);font-size:42px;line-height:1.15;font-weight:400;text-shadow:0 2px 6px rgba(0,0,0,.35)}
.hero-title b{font-weight:700}
.find-bar{top:637px;height:64px;background:var(--green-dark)}
.bin-visual{position:absolute;left:193px;top:-52px;width:120px;height:114px;background:
  linear-gradient(90deg,rgba(0,0,0,.18) 0 8%,rgba(0,0,0,0) 8% 92%,rgba(0,0,0,.18) 92%),
  linear-gradient(#7ccd4a,#3f9a23 60%,#2f7f1f)}
.find-bar .label{position:absolute;left:333px;top:16px;color:var(--white);font-size:19px;font-weight:600;display:flex;align-items:center;gap:14px}
.zip{position:absolute;width:186px;height:34px;background:var(--white);color:#888;font-size:13px;padding:8px 10px}
.search-btn{position:absolute;background:var(--yellow);color:var(--ink);font-weight:700;font-size:13px;padding:9px 24px}

/* welcome */
.welcome{top:701px;height:415px}
.welcome h2{position:absolute;left:172px;top:56px;font-size:30px;font-weight:400;display:flex;align-items:center;gap:10px}
.welcome h2 .logo-mark{width:40px;height:40px}
.welcome h2 b{font-weight:700}
.welcome p{position:absolute;left:172px;top:128px;width:560px;font-size:13.5px;line-height:1.95;color:#444}
.welcome .btn-more{position:absolute;left:172px;top:336px}
.store-visual{position:absolute;left:758px;top:126px;width:264px;height:178px;border:4px solid #ddd;background:
  linear-gradient(180deg,#6b8a4a 0 18%,rgba(0,0,0,0) 18%),
  radial-gradient(ellipse 60px 40px at 200px 120px,#e6d86a 0%,rgba(230,216,106,0) 100%),
  linear-gradient(180deg,#cfd6dc 0 18%,#8e9aa2 18% 40%,#55606a 40% 80%,#9a9a94 80%)}

/* values */
.values{top:1116px;height:346px;background:
  radial-gradient(ellipse 260px 180px at 300px 150px,#4f8f2a 0%,rgba(79,143,42,0) 100%),
  radial-gradient(ellipse 280px 200px at 750px 140px,#3f7f26 0%,rgba(63,127,38,0) 100%),
  radial-gradient(ellipse 120px 110px at 200px 60px,#d8d2c6 0%,rgba(216,210,198,0) 100%),
  radial-gradient(ellipse 90px 170px at 1020px 220px,#1f2a1d 0%,rgba(31,42,29,0) 100%),
  linear-gradient(180deg,#4b4d48 0%,#3a3c37 60%,#2a2b28 100%)}
.value-card{position:absolute;width:200px;height:92px;background:var(--green-mid);color:var(--white);font-size:13px;font-weight:700;padding:14px 10px 0 56px;line-height:1.4;box-shadow:0 2px 6px rgba(0,0,0,.3)}
.value-card svg{position:absolute;left:14px;top:14px;width:30px;height:30px}

/* recipients */
.recipients{top:1462px;height:501px;background:var(--grey-bg)}
.recipients .logo-mark{position:absolute;left:340px;top:66px;width:80px;height:80px}
.recipients h2{position:absolute;left:178px;top:156px;font-size:33px;font-weight:700;color:#222;white-space:nowrap}
.recipients .sub{position:absolute;left:237px;top:203px;font-size:14px}
.recipients .btn-more{position:absolute;left:333px;top:238px}
.level{position:absolute;width:150px}
.level .tag{background:var(--green);color:var(--white);text-align:center;font-weight:700;font-size:14px;line-height:1.3;padding:6px 0;border-radius:3px}
.level .bar{position:absolute;left:49px;width:52px;background:var(--yellow)}
.level .bar i{position:absolute;left:10px;bottom:14px;width:32px;height:32px;background:var(--green-light);border:3px solid var(--green)}
.baseline{position:absolute;left:430px;top:437px;width:600px;height:3px;background:#cfcfcf}

/* how it works */
.how-title{top:1963px;height:99px;background:var(--green-mid)}
.how-title h2{text-align:center;color:var(--white);font-size:48px;font-weight:700;line-height:99px}
.how{top:2062px;height:370px;background:var(--green-light)}
.step{position:absolute;width:250px;text-align:center}
.step .circle{position:relative;width:128px;height:128px;border-radius:50%;background:var(--yellow);border:5px solid var(--green);margin:0 auto}
.step .circle svg{position:absolute;left:34px;top:34px;width:50px;height:50px}
.step .num{position:absolute;left:-14px;top:8px;width:40px;height:40px;border-radius:50%;background:var(--red);color:var(--white);font-weight:700;font-size:14px;line-height:36px;border:2px solid var(--white)}
.step p{margin-top:40px;font-size:14px;line-height:1.5}
.how .btn-more{position:absolute;left:548px;top:296px}
.how .connect{position:absolute;top:74px}

/* news */
.news{top:2432px;height:675px}
.news h2{position:absolute;left:172px;top:52px;font-size:30px;font-weight:700}
.news-item{position:absolute;left:172px;width:416px;height:104px;background:var(--green-pale);display:flex;gap:14px;padding:11px 12px}
.news-item .thumb{flex:0 0 82px;width:82px;height:82px;background:var(--white);display:flex;align-items:center;justify-content:center}
.news-item .thumb i{width:40px;height:40px;background:var(--yellow);border:3px solid var(--green)}
.news-item .thumb.photo{background:radial-gradient(ellipse 30px 36px at 45px 40px,#e2b9a0 0%,rgba(226,185,160,0) 100%),linear-gradient(#8c5a4a,#5c3e36)}
.news-item h4{font-size:13px;font-weight:400;line-height:1.4;margin-top:3px}
.news-item small{display:block;font-size:10px;color:#666;margin-top:5px}
.news .btn-more{position:absolute;left:172px;top:594px}
.promo{position:absolute;left:612px;top:57px;width:415px;height:555px;background:var(--yellow);overflow:hidden}
.promo h3{font-family:"Playfair Display",Georgia,serif;color:var(--green-dark);font-weight:700;font-size:25px;text-align:center;line-height:1.25;padding:24px 22px 0}
.promo .band{position:absolute;left:0;top:132px;width:415px;height:175px;background:var(--green-dark);clip-path:polygon(0 0,50% 22%,100% 0,100% 100%,0 100%)}
.promo .band p{position:absolute;top:52px;width:100%;text-align:center;color:var(--white);font-family:"Playfair Display",Georgia,serif;font-weight:700;font-size:32px;line-height:1.05}
.promo .band p span{display:block;color:var(--yellow);font-size:32px}
.promo .pic{position:absolute;left:40px;top:312px;width:335px;height:150px;background:
  radial-gradient(ellipse 70px 60px at 60px 90px,#f0d6c4 0%,rgba(240,214,196,0) 100%),
  radial-gradient(ellipse 50px 70px at 210px 80px,#2c2c34 0%,rgba(44,44,52,0) 100%),
  radial-gradient(ellipse 40px 60px at 290px 90px,#e8e4dc 0%,rgba(232,228,220,0) 100%),
  linear-gradient(90deg,#cdb8a6,#9c8a7c 55%,#c4b6a6)}
.promo .logo-mark{position:absolute;left:183px;top:448px;width:48px;height:48px}
.promo .btn-more{position:absolute;left:161px;top:508px}

/* bins map */
.bins{top:3107px;height:300px}
.bins-panel{position:absolute;left:0;top:0;width:444px;height:300px;background:var(--green-dark);color:var(--white);text-align:center;padding-top:38px}
.bins-panel .logo-mark{width:76px;height:76px}
.bins-panel h3{font-family:"Playfair Display",Georgia,serif;font-weight:400;font-size:22px;margin-top:18px}
.bins-panel .icons{margin-top:12px;display:flex;justify-content:center;gap:22px}
.bins-panel p{font-size:13px;margin-top:10px;line-height:1.3}
.map-visual{position:absolute;left:444px;top:0;width:756px;height:300px;background:
  radial-gradient(ellipse 260px 200px at 720px 280px,#9cc6e4 0%,#a9cde6 50%,rgba(169,205,230,0) 100%),
  radial-gradient(ellipse 160px 70px at 300px 40px,#a9cde6 0%,rgba(169,205,230,0) 100%),
  radial-gradient(ellipse 120px 150px at 330px 170px,#d8e4b8 0%,rgba(216,228,184,0) 100%),
  radial-gradient(ellipse 220px 140px at 560px 110px,#cfe2c0 0%,rgba(207,226,192,0) 100%),
  linear-gradient(120deg,#ece5cf,#e3e4cb 50%,#d6e3cc)}

/* footer */
.site-footer{top:3407px;height:297px;background:var(--green-light)}
.foot-col{position:absolute;top:36px;font-size:11.5px;line-height:1.55}
.foot-col h5{font-size:11.5px;font-weight:700;margin-bottom:10px}
.social{display:flex;gap:8px}
.social i{width:28px;height:28px;border-radius:50%;border:2px solid var(--ink)}
.foot-find h5{font-size:19px;font-weight:600}
.badges{position:absolute;left:755px;top:158px;display:flex;gap:24px}
.badges i{width:48px;height:48px;border-radius:50%;border:3px solid #55705a}
.badges i.seal{background:var(--yellow);border-color:#c9a300}
.copyright{position:absolute;left:172px;top:266px;font-size:11px}
</style>
</head>
<body>

<header class="site-header">
  <div class="brand">
    <span class="logo-mark"></span>
    <div><div class="brand-name">BRIGHTWELL GIVING</div><div class="brand-tag">Think Globally while Donating Locally</div></div>
  </div>
  <div class="contact-phones">
    <svg class="phone-icon" viewBox="0 0 24 24"><path fill="#3b6e1d" d="M6.6 10.8c1.4 2.8 3.8 5.1 6.6 6.6l2.2-2.2c.3-.3.7-.4 1-.2 1.1.4 2.3.6 3.6.6.6 0 1 .4 1 1V20c0 .6-.4 1-1 1C10.6 21 3 13.4 3 4c0-.6.4-1 1-1h3.5c.6 0 1 .4 1 1 0 1.3.2 2.5.6 3.6.1.3 0 .7-.2 1z"/></svg>
    <div class="phone-block">Toll Free:<b>(800) 555-0142</b></div>
    <div class="phone-block">New York:<b>(800) 555-0198</b></div>
  </div>
  <div class="donate-now">DONATE NOW</div>
</header>

<nav class="main-nav">
  <ul>
    <li class="active">HOME</li><li>MISSIONS ▾</li><li>HOW IT WORKS</li><li>ABOUT US ▾</li><li>SPONSORS</li><li>NEWS</li><li>DONATE</li><li>WALL OF NEEDS</li>
  </ul>
</nav>

<section class="hero" role="img" aria-label="Volunteer smiling while holding donated clothing in a donation center">
  <h1 class="hero-title serif">Think Globally While<br>Donationg Locally<br><b>Brightwell Giving</b></h1>
</section>

<section class="find-bar">
  <div class="bin-visual" role="img" aria-label="Green clothing donation bin"></div>
  <div class="label">
    <svg width="34" height="30" viewBox="0 0 34 30"><path d="M17 2a7 7 0 0 0-7 7c0 5 7 12 7 12s7-7 7-12a7 7 0 0 0-7-7z" fill="none" stroke="#fff" stroke-width="2"/><circle cx="17" cy="9" r="2.5" fill="#fff"/><path d="M4 28l6-8h14l6 8z" fill="none" stroke="#fff" stroke-width="2"/></svg>
    Find Local Donation Place
  </div>
  <div class="zip" style="left:654px;top:15px">Zip</div>
  <div class="search-btn" style="left:854px;top:15px">SEARCH</div>
</section>

<section class="welcome">
  <h2 class="serif">WELCOME TO <span class="logo-mark"></span><b>BRIGHTWELL GIVING</b></h2>
  <p>Brightwell Giving is a non-profit organization that was created for one purpose: helping the less fortunate in our country's time of greatest need. Started in 2001, Brightwell Giving has been a dedicated member of its local communities over the past four years. The company's clothing collection efforts have allowed it to provide some of the neediest members of the community to clothe themselves and their families. The company's goal is to ensure that some of the most basic needs of the community's members are met thru the philanthropic efforts of the organizations members and contributors.</p>
  <span class="btn-more">READ MORE ▸</span>
  <div class="store-visual" role="img" aria-label="Thrift store storefront with a ribbon-cutting opening"></div>
</section>

<section class="values" role="img" aria-label="Green clothing donation bins loaded on a truck with a staff member beside them">
  <div class="value-card" style="left:272px;top:69px"><svg viewBox="0 0 30 30"><circle cx="15" cy="15" r="15" fill="#ffd200"/><text x="15" y="25" text-anchor="middle" font-size="22" font-weight="700" fill="#3b6e1d">“</text></svg>We Are An Open Book Organization</div>
  <div class="value-card" style="left:500px;top:69px"><svg viewBox="0 0 30 30"><circle cx="15" cy="15" r="15" fill="#ffd200"/><text x="15" y="25" text-anchor="middle" font-size="22" font-weight="700" fill="#3b6e1d">“</text></svg>We Are A True 501(C)(3) Non-Profit Organization</div>
  <div class="value-card" style="left:728px;top:69px"><svg viewBox="0 0 30 30"><circle cx="15" cy="15" r="15" fill="#ffd200"/><text x="15" y="25" text-anchor="middle" font-size="22" font-weight="700" fill="#3b6e1d">“</text></svg>Our Goal Is To Be With And Within The Community</div>
  <div class="value-card" style="left:272px;top:193px"><svg viewBox="0 0 30 30"><circle cx="15" cy="15" r="15" fill="#ffd200"/><text x="15" y="25" text-anchor="middle" font-size="22" font-weight="700" fill="#3b6e1d">“</text></svg>Support Anti-Gun Violence</div>
  <div class="value-card" style="left:500px;top:193px"><svg viewBox="0 0 30 30"><circle cx="15" cy="15" r="15" fill="#ffd200"/><text x="15" y="25" text-anchor="middle" font-size="22" font-weight="700" fill="#3b6e1d">“</text></svg>Help Disaster Victims Of Hurricane Irene</div>
  <div class="value-card" style="left:728px;top:193px"><svg viewBox="0 0 30 30"><circle cx="15" cy="15" r="15" fill="#ffd200"/><text x="15" y="25" text-anchor="middle" font-size="22" font-weight="700" fill="#3b6e1d">“</text></svg>Help Northbrook Family &amp; Child Society</div>
</section>

<section class="recipients">
  <span class="logo-mark"></span>
  <h2 class="serif">DONATION RECEPIENTS</h2>
  <div class="sub">Think Globally while Donating Locally</div>
  <span class="btn-more">READ MORE ▸</span>
  <div class="baseline"></div>
  <div class="level" style="left:452px;top:301px"><div class="tag">LEVEL 1<br>$1000</div><div class="bar" style="top:50px;height:86px"><i></i></div></div>
  <div class="level" style="left:560px;top:237px"><div class="tag">LEVEL 2<br>$1000-$2500</div><div class="bar" style="top:50px;height:150px"><i></i></div></div>
  <div class="level" style="left:668px;top:168px"><div class="tag">LEVEL 3<br>$2500-$5000</div><div class="bar" style="top:50px;height:219px"><i></i></div></div>
  <div class="level" style="left:774px;top:118px"><div class="tag">LEVEL 4<br>$5000-$10000</div><div class="bar" style="top:50px;height:269px"><i></i></div></div>
  <div class="level" style="left:878px;top:61px"><div class="tag">LEVEL 5<br>$10,000-$25000</div><div class="bar" style="top:50px;height:326px"><i></i></div></div>
</section>

<section class="how-title"><h2 class="serif">HOW IT WORKS</h2></section>
<section class="how">
  <svg class="connect" style="left:370px" width="190" height="40" viewBox="0 0 190 40"><path d="M2 26 Q95 2 180 22" fill="none" stroke="#fff" stroke-width="2" stroke-dasharray="5 4"/><path d="M175 16l9 6-9 5" fill="none" stroke="#fff" stroke-width="2"/></svg>
  <svg class="connect" style="left:655px" width="190" height="40" viewBox="0 0 190 40"><path d="M2 18 Q95 40 180 22" fill="none" stroke="#fff" stroke-width="2" stroke-dasharray="5 4"/><path d="M175 17l9 5-9 6" fill="none" stroke="#fff" stroke-width="2"/></svg>
  <div class="step" style="left:166px;top:56px">
    <div class="circle"><span class="num">01</span><svg viewBox="0 0 50 50"><rect x="8" y="6" width="34" height="38" rx="3" fill="none" stroke="#2b2b2b" stroke-width="3"/><path d="M18 18l4-4h6l4 4-3 3v10H21V21z" fill="#2b2b2b"/></svg></div>
    <p>Drop off clothing at your<br>closest donation bin.</p>
  </div>
  <div class="step" style="left:450px;top:56px">
    <div class="circle"><span class="num">02</span><svg viewBox="0 0 50 50"><rect x="4" y="14" width="28" height="20" fill="none" stroke="#2b2b2b" stroke-width="3"/><path d="M32 20h8l6 7v7H32z" fill="none" stroke="#2b2b2b" stroke-width="3"/><circle cx="13" cy="37" r="4" fill="#2b2b2b"/><circle cx="38" cy="37" r="4" fill="#2b2b2b"/></svg></div>
    <p>We pick it up and take it to our<br>sorting facility</p>
  </div>
  <div class="step" style="left:764px;top:56px">
    <div class="circle"><span class="num">03</span><svg viewBox="0 0 50 50"><circle cx="30" cy="18" r="11" fill="none" stroke="#2b2b2b" stroke-width="3"/><text x="30" y="23" text-anchor="middle" font-size="13" font-weight="700" fill="#2b2b2b">$</text><path d="M4 36h10l10 4 14-6v6l-14 6-10-4H4z" fill="none" stroke="#2b2b2b" stroke-width="3"/></svg></div>
    <p>Charities get clothing. We pay<br>you for the clothes.</p>
  </div>
  <span class="btn-more">READ MORE ▸</span>
</section>

<section class="news">
  <h2 class="serif">RECENT NEWS</h2>
  <div class="news-item" style="top:114px"><div class="thumb"><i></i></div><div><h4>Brightwell Giving created the flyer for inform the people in Manhattan to help others by giving donation.</h4><small>MAY 16, 2017 • CATEGORIES: MAIN • BY ADMIN</small></div></div>
  <div class="news-item" style="top:228px"><div class="thumb"><i></i></div><div><h4>We are starting the charity projects to collect funds on FundBridge</h4><small>APRIL 28, 2017 • CATEGORIES: MAIN • BY ADMIN</small></div></div>
  <div class="news-item" style="top:342px"><div class="thumb photo" role="img" aria-label="Child at a charity event"></div><div><h4>CHARITY PROJECT LOVE THY NEIGHBOR-ELENA</h4><small>APRIL 18, 2017 • CATEGORIES: MAIN • BY ADMIN</small></div></div>
  <div class="news-item" style="top:456px"><div class="thumb"><i></i></div><div><h4>Charity Project LOVE THY NEIGHBOR donation boxes</h4><small>APRIL 15, 2017 • CATEGORIES: MAIN • BY ADMIN</small></div></div>
  <span class="btn-more">READ MORE ▸</span>
  <div class="promo">
    <h3>Brightwell Giving Donated to Orphan House In Ukraine</h3>
    <div class="band"><p>DONATION<br>IN EUROPE<span>“UKRAINE”</span></p></div>
    <div class="pic" role="img" aria-label="Children and volunteers at an orphan house"></div>
    <span class="logo-mark"></span>
    <span class="btn-more">READ MORE ▸</span>
  </div>
</section>

<section class="bins">
  <div class="bins-panel">
    <span class="logo-mark"></span>
    <h3>Brightwell Giving Bins</h3>
    <div class="icons">
      <svg width="24" height="24" viewBox="0 0 24 24"><path d="M12 2l3 7 7 .5-5.5 4.5 2 7-6.5-4-6.5 4 2-7L2 9.5 9 9z" fill="none" stroke="#fff" stroke-width="1.5"/></svg>
      <svg width="24" height="24" viewBox="0 0 24 24"><circle cx="18" cy="5" r="3" fill="none" stroke="#fff" stroke-width="1.5"/><circle cx="6" cy="12" r="3" fill="none" stroke="#fff" stroke-width="1.5"/><circle cx="18" cy="19" r="3" fill="none" stroke="#fff" stroke-width="1.5"/><path d="M8.6 10.7l6.8-4M8.6 13.3l6.8 4" stroke="#fff" stroke-width="1.5"/></svg>
      <svg width="24" height="24" viewBox="0 0 24 24"><path d="M3 9V3h6M15 3h6v6M21 15v6h-6M9 21H3v-6" fill="none" stroke="#fff" stroke-width="1.5"/></svg>
    </div>
    <p>Clothes Donation Bins<br>16,368 views</p>
  </div>
  <div class="map-visual" role="img" aria-label="Map of the northeastern region marking donation bin locations"></div>
</section>

<footer class="site-footer">
  <div class="foot-col" style="left:172px"><h5>QUICK LINKS</h5>Home<br>Missions<br>How It Works<br>About Us<br>Sponsors<br>News<br>Donate<br>Wall Of Needs</div>
  <div class="foot-col" style="left:331px"><h5>CONTACT US</h5>New York Office<br>42 Orchard Ln, Millbrook, NY 12001<br>(800) 555-0142<br><br>NY Warehouse<br>915 River Rd, Fairhaven, NY 12402<br><br>Thrift Store<br>218 Elm St Lakeside, NY 12500</div>
  <div class="foot-col" style="left:543px"><h5>FOLLOW US</h5><div class="social"><i></i><i></i><i></i></div></div>
  <div class="foot-col foot-find" style="left:755px;top:30px"><h5>Find Local Donation Place</h5></div>
  <div class="zip" style="left:755px;top:80px;height:36px">Zip</div>
  <div class="search-btn" style="left:940px;top:80px">SEARCH</div>
  <div class="badges"><i></i><i></i><i></i><i class="seal"></i></div>
  <div class="copyright">© 2018 Brightwell Giving. All Rights Reserved.</div>
</footer>

</body>
</html>
```